Influencer Marketing Präsentation
Zielgruppe
Ich: Influencer
Anlass: Weiterbildungs-Tagung
Zielgruppe: Teilnehmer der Digital Marketing-Weiterbildung, welche zeitgleich auch Marketing-Leute sind von Unternehmen, die etwas über Influencer Marketing erfahren möchten.
Aufgabenstellung
Ich benötige eine pfannenfertige PPTX Präsentation für meinen Vortrag an einer Digital-Marketing Tagung!
Die Präsentation ist 20min maximal, plus 10min Q&A. Sie soll cool daherkommen, aber nicht zu verspielt. Die Leute sollen sich auch denken 'wow, der hat nicht nur was als Influencer auf dem Kasten, sondern hat auch eine coole PPT zu seinem Vortrag!' Da den ganzen Tag lang unterschiedliche Leute präsentieren zu verschiedensten Marketing Themen, will ich die Präsentation locker und cool gestalten und nicht zu heftig mit Zahlen und schwerem Inhalt.
Die angehängte PPT ist ein Mix aus zwei 'alten' Präsentationen, welche ich zu dem Thema gemacht habe. Nun gilt es, die coolsten Themen rauszupicken, diese bei Bedarf auf Deutsch zu übersetzen, und allenfalls noch andere Influencer-Marketing Themen, Tips & tricks einzubauen.
Im ersten Slide der angehängten Präsentation siehst Du ein Inhaltsverzeichnis. so stelle ich mir das in etwa vor. bin aber auch offen, das ganze zu straffen!
Hier noch ein Link zu einer online verfügbaren Präsentation, von welcher ich folgende Slides integrieren möchte (anders darstellen und Umtexten bitte, damit man nicht 1:1 kopiert!) https://folienkiste.example/slide/48213907/
Slides: 5, 6, 7, 8, 11. Können auch zusammengefasst werden auf 2-3 slides!
Das fertige Projekt (Präsentation) sollte im PPTX Format angeliefert werden, so dass ich allenfalls noch letzte inhaltliche Korrekturen anbringen kann.

```html
<!DOCTYPE html>
<html lang="de">
<head>
<meta charset="UTF-8">
<title>Mikro Makro Influencer – Titelfolie</title>
<link rel="stylesheet" href="https://fonts.googleapis.com/css2?family=Anton&family=Playfair+Display:wght@700&display=swap">
<style>
  :root {
    --ink: #0d0d0d;
    --paper: #ffffff;
    --accent: #a41e22;
    --photo-light: #d9d9d9;
    --photo-mid: #9a9a9a;
    --photo-dark: #2a2a2a;
  }
  html, body {
    margin: 0;
    padding: 0;
    width: 1200px;
    height: 674px;
    overflow: hidden;
    background: var(--paper);
  }
  .slide {
    position: relative;
    width: 1200px;
    height: 674px;
    overflow: hidden;
    background: var(--paper);
  }
  .hero-photo {
    position: absolute;
    left: 0;
    top: 0;
    width: 534px;
    height: 674px;
    background:
      radial-gradient(ellipse at 45% 50%, var(--photo-light) 0%, var(--photo-mid) 45%, transparent 75%),
      linear-gradient(160deg, var(--photo-dark) 0%, var(--photo-mid) 40%, var(--photo-light) 70%, var(--photo-mid) 100%);
  }
  .title-panel {
    position: absolute;
    left: 534px;
    top: 0;
    width: 666px;
    height: 674px;
  }
  .subtitle {
    font-family: "Playfair Display", Georgia, serif;
    font-weight: 700;
    fill: var(--ink);
  }
  .headline-block {
    font-family: "Anton", "Impact", sans-serif;
    fill: var(--ink);
  }
  .headline-serif {
    font-family: "Playfair Display", Georgia, serif;
    font-weight: 700;
    fill: var(--ink);
  }
  .brand-name {
    font-family: "Playfair Display", Georgia, serif;
    font-weight: 700;
    fill: var(--ink);
  }
  .brand-dot {
    fill: var(--accent);
  }
</style>
</head>
<body>
  <main class="slide">
    <div class="hero-photo" role="img" aria-label="Schwarzweißfoto: Babyhand umgreift den Finger eines Erwachsenen"></div>

    <svg class="title-panel" width="666" height="674" viewBox="534 0 666 674" xmlns="http://www.w3.org/2000/svg">
      <text class="subtitle" x="590" y="61" font-size="27" textLength="550" lengthAdjust="spacingAndGlyphs">BERÜHMTHEITEN VS NISCHENEINFLUSS</text>

      <g transform="translate(691,0) rotate(-90)">
        <text class="headline-block" x="-700" y="0" font-size="190" textLength="371" lengthAdjust="spacingAndGlyphs">MIKRO</text>
      </g>
      <g transform="translate(832,0) rotate(-90)">
        <text class="headline-block" x="-700" y="0" font-size="190" textLength="408" lengthAdjust="spacingAndGlyphs">MAKRO</text>
      </g>
      <g transform="translate(902,0) rotate(-90)">
        <text class="headline-serif" x="-672" y="0" font-size="94" textLength="517" lengthAdjust="spacingAndGlyphs">INFLUENCER</text>
      </g>

      <g class="brand">
        <circle class="brand-dot" cx="1011" cy="547" r="12"/>
        <text class="brand-name" x="1030" y="555" font-size="22">Ankerpunkt</text>
      </g>
    </svg>
  </main>
</body>
</html>
```